Design Box Packaging with Logo for a high-end menswear store

I would like to come up with a design for our shipping boxes.
- Printing would only be in 1 colour. (box will be in mid beige/brown)
- I want it to look modern and clean
- I have attached my logo
- It is for a high-end menswear store for shipping clothing for online purchases
Size of the box is about 14 x 10 x 5

Target Market(s)

High-end / wealthy people shopping online

Industry/Entity Type

Clothing, retail, online high-end clothing

Colors

Designer to choose colors to be used in the design.

Requirements
Must have
• Look sharp and clean, have logo information, online printing one colour
Nice to have
• Look clean and modern

```html
<!DOCTYPE html>
<html lang="en">
<head>
<meta charset="UTF-8">
<title>Marlowe Boutique – Shipping Box Panels</title>
<link href="https://fonts.googleapis.com/css2?family=Montserrat:wght@400&family=Open+Sans:wght@400&display=swap" rel="stylesheet">
<style>
  :root {
    --page: #ffffff;
    --kraft: #c69c6d;
    --kraft-light: #cfa77a;
    --ink: #1c1a18;
    --brush: #ffffff;
    --shadow: rgba(0, 0, 0, 0.28);
  }
  * { margin: 0; padding: 0; box-sizing: border-box; }
  html, body {
    width: 1200px;
    height: 1200px;
    overflow: hidden;
    background: var(--page);
  }
  .sheet {
    position: relative;
    width: 1200px;
    height: 1200px;
  }
  .sheet-backing {
    position: absolute;
    left: 30px; top: 120px;
    width: 1142px; height: 857px;
    background: var(--page);
    box-shadow: 0 18px 28px -10px var(--shadow);
  }
  .panel {
    position: absolute;
    overflow: hidden;
    background: radial-gradient(ellipse at 40% 40%, var(--kraft-light), var(--kraft));
  }
  .panel--lid   { left: 30px;  top: 122px; width: 830px; height: 235px; }
  .panel--front { left: 30px;  top: 377px; width: 830px; height: 596px; }
  .panel--side  { left: 873px; top: 379px; width: 297px; height: 596px; }

  .brush-stroke {
    position: absolute;
    background: linear-gradient(90deg, rgba(255,255,255,0) 0%, var(--brush) 45%, var(--brush) 75%, rgba(255,255,255,0.4) 100%);
    border-radius: 40% 10% 40% 10% / 8% 50% 8% 50%;
  }
  .panel--lid .brush-stroke   { right: 0; top: 0; width: 54px; height: 235px; }
  .panel--front .brush-stroke {
    left: 0; top: 10px; width: 95px; height: 586px;
    background: linear-gradient(270deg, rgba(255,255,255,0) 0%, var(--brush) 45%, var(--brush) 80%, rgba(255,255,255,0.6) 100%);
  }
  .panel--side .brush-stroke  { right: 0; top: 0; width: 96px; height: 596px; }

  .wordmark {
    position: absolute;
    display: flex;
    flex-direction: column;
    align-items: center;
    font-family: "Montserrat", sans-serif;
    font-weight: 400;
    color: var(--ink);
    text-align: center;
    white-space: nowrap;
  }
  .wordmark__name { text-transform: uppercase; }
  .wordmark__tag  { text-transform: uppercase; }

  .panel--lid .wordmark { left: 305px; top: 82px; width: 260px; }
  .panel--lid .wordmark__name { font-size: 30px; letter-spacing: 0.08em; }
  .panel--lid .wordmark__tag  { font-size: 10px; letter-spacing: 0.55em; margin-top: 14px; }

  .panel--front .wordmark { left: 470px; top: 148px; width: 340px; }
  .panel--front .wordmark__tag  { font-size: 19px; letter-spacing: 0.6em; order: -1; }
  .panel--front .wordmark__name { font-size: 62px; letter-spacing: 0.06em; margin-top: 110px; }

  .panel--side .wordmark { left: 38px; top: 248px; width: 160px; }
  .panel--side .wordmark__tag  { font-size: 9px; letter-spacing: 0.45em; order: -1; }
  .panel--side .wordmark__name { font-size: 26px; letter-spacing: 0.06em; margin-top: 22px; }

  .fine-print {
    position: absolute;
    font-family: "Open Sans", sans-serif;
    font-size: 11px;
    color: var(--ink);
  }
  .panel--front .fine-print { left: 135px; top: 541px; }
  .panel--side .fine-print  { left: 45px;  top: 844px; top: 845px; }
  .panel--side .fine-print  { top: 845px; }
</style>
</head>
<body>
  <main class="sheet">
    <div class="sheet-backing"></div>

    <section class="panel panel--lid">
      <div class="brush-stroke" role="img" aria-label="White dry-brush stroke along the edge"></div>
      <div class="wordmark">
        <span class="wordmark__name">Marlowe</span>
        <span class="wordmark__tag">Boutique</span>
      </div>
    </section>

    <section class="panel panel--front">
      <div class="brush-stroke" role="img" aria-label="White dry-brush stroke along the edge"></div>
      <div class="wordmark">
        <span class="wordmark__name">Marlowe</span>
        <span class="wordmark__tag">Boutique</span>
      </div>
      <p class="fine-print">Lorem ipsum Lorem ipsum</p>
    </section>

    <section class="panel panel--side">
      <div class="brush-stroke" role="img" aria-label="White dry-brush stroke along the edge"></div>
      <div class="wordmark">
        <span class="wordmark__name">Marlowe</span>
        <span class="wordmark__tag">Boutique</span>
      </div>
      <p class="fine-print" style="top:845px;left:45px;position:absolute;">Lorem ipsum Lorem ipsum</p>
    </section>
  </main>
</body>
</html>
```